BUSINESS CARD - HALVERDINE RURAL SERVICES

I would like to create a business card for my fertilizer spreading business. I would like to incorporate my existing logo and also a description of the services offered. The business card will be given to farmers so must be kept simple but effective. It will also be left in stores so much also be eye catching in order to stand out from other cards.

Target Market(s)

FARMERS

Requirements
Must have
• FRONT OF CARD = EXISTING LOGO + "CUSTOMISED SPREADING" below the logo

REAR Of CARD = SERVICES OFFERED AND CONTACT DETAILS

- Bulk fertilizer including Lime, Gypsum, Manure & Compost
- Granular fertilizer including Single Super, Urea, Ammo-Gran, & Custom Blends
- Modern equipment - Autosteer & Variable Rate Capable
- Friendly & Reliable Service
- Contact Gus: 0471 502 318
Nice to have
• utilize same color scheme as existing logo

```html
<!DOCTYPE html>
<html lang="en">
<head>
<meta charset="utf-8">
<title>Halverdine Rural Services – Business Card</title>
<link rel="stylesheet" href="https://fonts.googleapis.com/css2?family=Open+Sans:wght@600;700&family=Roboto:wght@400;500&family=Arimo:wght@700&display=swap">
<style>
  :root {
    --stage: #d6d4d5;
    --card: #ffffff;
    --orange: #f39220;
    --charcoal: #58585a;
    --text: #4a4a4c;
  }
  * { margin: 0; padding: 0; box-sizing: border-box; }
  html, body {
    width: 1200px; height: 1100px; overflow: hidden;
    background: var(--stage);
  }
  .canvas { position: relative; width: 1200px; height: 1100px; }

  .card {
    position: absolute; left: 259px; width: 705px; height: 405px;
    background: var(--card); border-radius: 22px; overflow: hidden;
  }
  .card--rear { top: 115px; }
  .card--front { top: 560px; }

  /* rear: services */
  .services-title {
    position: absolute; left: 42px; top: 36px; line-height: 1;
    font-family: "Open Sans", sans-serif; font-weight: 600;
    font-size: 27px; color: var(--orange); letter-spacing: 0.2px;
  }
  .services-list {
    position: absolute; left: 42px; top: 76px; list-style: none;
    font-family: "Roboto", sans-serif; font-size: 17.5px; line-height: 24px;
    color: var(--text);
  }
  .services-list li::before {
    content: "•"; color: var(--orange); margin-right: 2px;
  }
  .decor-area {
    position: absolute; left: 0; top: 173px; width: 270px; height: 232px;
  }
  .contact-label {
    position: absolute; right: 40px; top: 274px; line-height: 1;
    font-family: "Arimo", sans-serif; font-weight: 700;
    font-size: 32px; color: var(--charcoal);
  }
  .phone-band {
    position: absolute; left: 328px; top: 316px; width: 377px; height: 51px;
  }
  .phone-number {
    position: absolute; left: 394px; top: 317px;
    font-family: "Arimo", sans-serif; font-weight: 700;
    font-size: 35px; color: #ffffff; letter-spacing: 1px; line-height: 50px;
  }
  .phone-icon { position: absolute; left: 637px; top: 326px; width: 30px; height: 30px; }

  /* front: identity */
  .brand-mark {
    position: absolute; left: 272px; top: 46px;
    width: 162px; height: 162px; border-radius: 50%;
    background: var(--charcoal);
  }
  .brand-name {
    position: absolute; left: 0; right: 0; top: 214px; text-align: center;
    font-family: "Open Sans", sans-serif; font-weight: 700; line-height: 1.3;
    font-size: 30px; color: var(--charcoal); letter-spacing: -0.3px;
  }
  .tagline {
    position: absolute; left: 0; right: 0; top: 342px; text-align: center;
    font-family: "Open Sans", sans-serif; font-weight: 600; line-height: 1.2;
    font-size: 22px; color: var(--orange); letter-spacing: 0.3px;
  }
</style>
</head>
<body>
<main class="canvas">
  <section class="card card--rear" aria-label="Business card rear">
    <h2 class="services-title">SERVICES OFFERED</h2>
    <ul class="services-list">
      <li>Bulk fertilizer including Lime, Gypsum, Manure &amp; Compost</li>
      <li>Granular fertilizer including Single Super, Urea, Ammo-Gran, &amp; Custom Blends</li>
      <li>Modern equipment - Autosteer &amp; Variable Rate Capable</li>
      <li>Friendly &amp; Reliable Service</li>
    </ul>
    <svg class="decor-area" viewBox="0 0 270 232" role="img" aria-label="Large decorative farm emblem area: livestock in a field under a grain stalk with an orange sprout">
      <defs>
        <linearGradient id="decorFade" x1="0" y1="0" x2="0" y2="1">
          <stop offset="0" stop-color="#f1f0f1"/>
          <stop offset="1" stop-color="#c9c8ca"/>
        </linearGradient>
      </defs>
      <path d="M0 232 V40 Q100 -10 230 40 V232 Z" fill="url(#decorFade)"/>
    </svg>
    <p class="contact-label">Contact Gus:</p>
    <svg class="phone-band" viewBox="0 0 377 51" aria-hidden="true">
      <polygon points="58,0 377,0 377,51 0,51" fill="var(--charcoal)"/>
    </svg>
    <p class="phone-number">0471 502 318</p>
    <svg class="phone-icon" viewBox="0 0 24 24" aria-hidden="true">
      <path fill="var(--orange)" d="M6.6 10.8c1.4 2.8 3.8 5.1 6.6 6.6l2.2-2.2c.3-.3.7-.4 1-.2 1.1.4 2.3.6 3.6.6.6 0 1 .4 1 1V20c0 .6-.4 1-1 1C10.6 21 3 13.4 3 4c0-.6.4-1 1-1h3.5c.6 0 1 .4 1 1 0 1.3.2 2.5.6 3.6.1.3 0 .7-.2 1L6.6 10.8z"/>
    </svg>
  </section>

  <section class="card card--front" aria-label="Business card front">
    <div class="brand-mark" aria-hidden="true"></div>
    <h1 class="brand-name">Halverdine Rural Services</h1>
    <p class="tagline">CUSTOMISED SPREADING</p>
  </section>
</main>
</body>
</html>
```